Label Redesign For Cannabis Pain Ointment

I have created a topical cannabis pain ointment for people with cancer to arthritis to skin conditions etc. It sells in medical marijuana dispensaries across BC Canada. I originally designed my really bad label myself out of urgency. Its come time to redesign it and make it more professional and eye catching.
My company is called "Drifting Heron". ***The label does not need to have anything to do with the willow tree.
Pictures of current bad label attached.
I need for this label to list the company name, the ointment name (Extra Strength Cannabis Ointment) and also the ingredients and directions. It will be a label that is wrapped around the jar (1.5 inches x 7.5 inches).
I want this label to be artistic. A piece of art in itself. I want it to take inspiration from concert posters or craft beer labels. I want it to be edgy, different, classy and sexy.
Ill attach pics of my current bad label (wood-grain, amateur, boring) and also a few shots of images that I like so you can get a sense of my style.
So looking forward to seeing what everyone can come up with.
Updates

Hi designers!Wanted to mention the label does not have to have anything to do with the willow tree. Willow tree images tend to be depressing and eventually I will have a small logo to put on the label.. For now, Id like the label to be simple and artsy, but am open to all kinds of suggestions. I open to more medical looking labels as long as it will stand out on the shelves. I am also open to vintage designs.Thank you for your time! Added Monday, May 16, 2016

Reason: I am extending the deadline because I am waiting for some designers to submit changes. Thank you very much!

Target Market(s)

All ages including but not limited to customers who do not ingest marijuana. Some patients want the benefits of the medicinal herb without the psychoactive effects.

Industry/Entity Type

Medical

Requirements
Must have
• Must be artistic.
Nice to have
• Mature, classy and super duper hip.
Should not have
• Cal Durrow or stereotypical cannabis smoking images.
• Does not need to have anything to do with willow trees.

```html
<!DOCTYPE html>
<html lang="en">
<head>
<meta charset="utf-8">
<title>Drifting Heron Ointment Label</title>
<link rel="stylesheet" href="https://fonts.googleapis.com/css2?family=League+Spartan:wght@700&family=Fredoka:wght@400;500&family=Montserrat:wght@700&display=swap">
<style>
  :root {
    --page: #ffffff;
    --navy: #0d3466;
    --deep: #13406f;
    --cyan: #3aa6bf;
    --ice: #dff4f7;
    --teal: #1a8a94;
    --teal-dark: #13707a;
    --frame: #8fc6cc;
    --orange: #ff7a1a;
    --ink: #0f2340;
    --lime: rgba(228, 251, 143, 0.9);
    --olive: rgba(190, 214, 110, 0.75);
  }
  html, body {
    margin: 0;
    padding: 0;
    width: 1200px;
    height: 1200px;
    overflow: hidden;
    background: var(--page);
  }
  .canvas {
    position: relative;
    width: 1200px;
    height: 1200px;
  }
  .label {
    position: absolute;
    left: 0;
    top: 390px;
    width: 1200px;
    height: 240px;
    overflow: hidden;
  }
  .label__art {
    position: absolute;
    inset: 0;
    background:
      radial-gradient(ellipse 260px 110px at 230px 225px, rgba(240, 250, 252, 0.97) 0%, rgba(240, 250, 252, 0.9) 55%, rgba(240, 250, 252, 0) 100%),
      linear-gradient(172deg, var(--navy) 0%, var(--deep) 40%, var(--cyan) 70%, var(--ice) 100%);
  }
  .accent-band {
    position: absolute;
    top: 0;
    height: 240px;
  }
  .accent-band--left { left: 336px; width: 74px; background: var(--lime); }
  .accent-band--right { left: 789px; width: 73px; background: var(--olive); }
  .title-box {
    position: absolute;
    left: 428px;
    top: 16px;
    width: 336px;
    height: 143px;
    box-sizing: border-box;
    background: #fff;
    border: 3px solid var(--frame);
    border-radius: 6px;
    display: flex;
    flex-direction: column;
    align-items: center;
    justify-content: center;
  }
  .title-box__name {
    margin: 0;
    font-family: "League Spartan", sans-serif;
    font-weight: 700;
    font-size: 56px;
    line-height: 54px;
    letter-spacing: -1px;
    color: var(--teal);
    text-align: center;
    padding-top: 6px;
  }
  .title-box__product {
    margin: 2px 0 0;
    font-family: "Fredoka", sans-serif;
    font-weight: 500;
    font-size: 11px;
    letter-spacing: 2px;
    text-transform: uppercase;
    color: var(--teal);
  }
  .ingredients {
    position: absolute;
    left: 430px;
    width: 340px;
    top: 170px;
    margin: 0;
    font-family: "Fredoka", sans-serif;
    font-size: 13.5px;
    line-height: 14.5px;
    color: var(--orange);
    text-align: center;
  }
  .directions {
    position: absolute;
    left: 440px;
    width: 320px;
    top: 213px;
    margin: 0;
    font-family: Arial, Helvetica, sans-serif;
    font-size: 8.3px;
    line-height: 10px;
    color: var(--ink);
    text-align: center;
  }
  .warnings {
    position: absolute;
    left: 180px;
    width: 160px;
    top: 180px;
    margin: 0;
    font-family: "Montserrat", sans-serif;
    font-weight: 700;
    font-size: 9.2px;
    line-height: 14px;
    color: var(--teal-dark);
    text-align: center;
  }
  .uses {
    position: absolute;
    left: 110px;
    width: 224px;
    top: 225px;
    margin: 0;
    font-family: "Fredoka", sans-serif;
    font-size: 9px;
    line-height: 11px;
    color: var(--teal-dark);
    text-align: right;
    white-space: nowrap;
  }
</style>
</head>
<body>
<div class="canvas">
  <section class="label">
    <div class="label__art" role="img" aria-label="Blue-toned photo collage of a striped modern building facade scattered with pale translucent triangles"></div>
    <div class="accent-band accent-band--left"></div>
    <div class="accent-band accent-band--right"></div>

    <p class="warnings">FOR TOPICAL USE ONLY<br>KEEP AWAY THIS PRODUCT<br>FROM KIDS AND PETS</p>
    <p class="uses">For bug bites, sunburn and other skin irritations.</p>

    <div class="title-box">
      <h1 class="title-box__name">DRIFTING<br>HERON</h1>
      <p class="title-box__product">Extra Strength Cannabis Ointment</p>
    </div>

    <p class="ingredients">Sweet Almond Oil, Mineral Oil, Avocado Oil, Honey<br>Ginger Extracts, Aqua, Hemp Buds &amp; Leaves</p>
    <p class="directions">Direction for Use: With the right amount of oinment,gently rub on your skin<br>that is affected. Reapply oinment as needed</p>
  </section>
</div>
</body>
</html>
```